freshen up existing wordpress site

We wish to re-implement our current wordpress website www.vormalux.com/web2.

The content, structure and menus of the website should remain the same, but style updated to a more fresh/contemporary layout. It must be wordpress based and use a highly modifiable template like Bright Panels Kora or similar.

Permalinks must be exactly as the old ones.

Landing page must contain a slider for images and movies, plus a little text. There is no requirement for a tab-style as seem on the current website.

The final result shall be transferred to a fresh multisite installation of wordpress, we will provide login for access later. If another method is better/more preferred, please comment and we can take it from there.

The two graphics on http://vormalux.com/web2/gridmarshal-product-details/ should be re-done to look more 'clean and professional' and look less powerpoint'ish. We will need the vectorfiles for edits later on. Color scheme is open, whatever matches with the the website style.

We work in a engineering-heavy B2B environment, so slightly conservative/boring styles; no 'pop smartness'. competitors websites looks like this:
- http://www.halvorix.com/
- http://www.quernaly.com/
- https://www.brasketo.com/products/ic_nanometer_design/
- https://www.wolvane-da.com/

Website background should be white for easy image implementation. Our Vormalux logo colors can be used where applicable ( #1C62A6 #2454A0 #EF0315 #FB3A37 ), and matching or complementary colors too.

Use Sans Serif fonts like googles or something like http://www.glyphmarten.com/fonts/noto-sans .

Target Market(s)

semiconductor industry

Number of Pages Required

5+ page

Font styles to use
Sans Serif

Requirements
Must have
• see above
Nice to have
• see above
Should not have
• not defined.

```html
<!DOCTYPE html>
<html lang="en">
<head>
<meta charset="utf-8">
<title>Vormalux</title>
<link href="https://fonts.googleapis.com/css2?family=Lato:wght@400;700;900&family=Questrial&family=Oswald:wght@400&display=swap" rel="stylesheet">
<style>
:root{
  --blue:#1c62a6;
  --blue-dark:#2454a0;
  --red:#ef0315;
  --ink:#2b2b2b;
  --text:#444;
  --rule:#dde6f1;
  --dark:#2e2e2e;
  --footer:#333436;
  --white:#fff;
}
*{box-sizing:border-box;margin:0;padding:0}
html,body{width:1200px;height:2493px;overflow:hidden;background:var(--white);font-family:"Lato",sans-serif;color:var(--text)}
.page{position:relative;width:1200px;height:2493px}
section,header,footer{position:absolute;left:0;width:1200px}

/* header */
.site-header{top:0;height:118px;background:linear-gradient(#fff,#f1f3f6);border-top:2px solid var(--blue);box-shadow:0 2px 4px rgba(0,0,0,.15);z-index:2}
.brand{position:absolute;left:98px;top:30px;display:flex;align-items:center;gap:10px}
.brand-square{width:40px;height:40px;background:var(--blue-dark)}
.brand-name{font-family:"Lato",sans-serif;font-weight:900;font-size:46px;color:var(--blue-dark);letter-spacing:-1px;line-height:1}
.top-contacts{position:absolute;right:98px;top:22px;display:flex;gap:28px;font-size:14px;color:var(--blue-dark);font-weight:700}
.top-contacts span{display:flex;align-items:center;gap:8px}
.main-nav{position:absolute;top:80px;left:560px;display:flex;gap:55px;font-size:14px;font-weight:700;color:var(--blue-dark);letter-spacing:.5px}
.main-nav .active{color:var(--red);border-bottom:2px solid var(--red);padding-bottom:6px}

/* hero */
.hero{top:118px;height:580px;background:radial-gradient(ellipse at 35% 40%,#5fbf6a 0%,#2f7a55 14%,#1a3e6e 32%,#0f2d5c 60%,#0a1f44 100%)}
.hero-caption{position:absolute;left:0;bottom:0;width:100%;height:108px;background:rgba(0,0,0,.72);display:flex;align-items:center;justify-content:center;text-align:center;font-family:"Oswald",sans-serif;color:#fff;font-size:32px;line-height:1.3}

/* common section heading */
.section-title{display:flex;align-items:center;justify-content:center;gap:14px;font-family:"Questrial",sans-serif;font-size:32px;color:var(--ink)}
.title-square{width:30px;height:30px;background:var(--blue-dark)}
.divider{position:relative;width:1000px;height:4px;background:var(--rule);margin:26px auto 0}
.divider::after{content:"";position:absolute;left:50%;top:-2px;width:8px;height:8px;margin-left:-4px;border-radius:50%;background:#9fb4cf}
.lead{width:1000px;margin:30px auto 0;text-align:center;font-size:13px;line-height:25px;color:var(--text)}

.welcome{top:698px;height:374px;padding-top:57px}
.btn{display:block;width:146px;height:37px;margin:24px auto 0;background:var(--blue-dark);color:#fff;font-size:13px;font-weight:700;text-align:center;line-height:37px;letter-spacing:.5px}

.about{top:1072px;height:523px;padding-top:54px;box-shadow:inset 0 8px 8px -6px rgba(0,0,0,.15)}
.steps{position:absolute;top:224px;left:0;width:1200px;height:230px}
.step{position:absolute;top:0;width:260px;text-align:center}
.step svg{display:block;margin:0 auto}
.step-label{margin-top:22px;font-size:18px;font-weight:700;color:var(--ink);line-height:24px}
.step-arrow{position:absolute;top:62px}

/* inquiry */
.inquiry{top:1595px;height:295px;background:radial-gradient(ellipse at 40% 30%,#4a4844,#2a2927 70%)}
.inquiry .section-title{color:#fff;padding-top:50px}
.inquiry .divider{background:#555;margin-top:26px;height:3px}
.inquiry .divider::after{background:#888}
.field{position:absolute;height:37px;background:#fff;font-size:11px;color:#555;padding-left:16px;line-height:37px;letter-spacing:.5px}
.submit{position:absolute;left:955px;top:198px;width:145px;height:37px;background:var(--blue-dark);color:#fff;font-size:13px;font-weight:700;text-align:center;line-height:37px}

/* news */
.news{top:1890px;height:320px;padding-top:52px}
.news-item{position:absolute;top:152px;width:470px;height:110px}
.news-photo{position:absolute;left:0;top:0;width:152px;height:108px;border:1px solid #ccc}
.news-body{position:absolute;left:172px;top:0;width:300px}
.news-body h3{font-size:14px;font-weight:700;color:var(--ink)}
.news-date{margin-top:14px;font-size:11px;color:var(--blue-dark);font-weight:700;display:flex;align-items:center;gap:8px}
.news-body p{margin-top:12px;font-size:11px;line-height:18px;color:#555}
.news-body p b{color:var(--blue-dark)}
.news-sep{position:absolute;left:599px;top:2042px;width:1px;height:108px;background:#ddd}

/* footer */
.site-footer{top:2210px;height:233px;background:var(--footer);color:#ddd}
.footer-col{position:absolute;top:50px}
.footer-col h4{font-family:"Questrial",sans-serif;font-size:20px;color:#fff;font-weight:400;padding-bottom:10px;border-bottom:1px solid #666}
.quick-links{list-style:none;margin-top:16px;font-size:13px;line-height:20.5px}
.quick-links li::before{content:"›";margin-right:10px}
.footer-col p{font-size:13px;margin-top:16px}
.email-box{margin-top:8px;width:228px;height:31px;background:#fff;font-size:11px;font-style:italic;color:#999;padding-left:10px;line-height:31px}
.gray-btn{margin-top:8px;width:117px;height:28px;background:#777;color:#fff;font-size:12px;font-weight:700;text-align:center;line-height:28px}
.contact-row{display:flex;align-items:flex-start;gap:14px;font-size:13px;line-height:21px;margin-top:14px}
.footer-mark{position:absolute;left:962px;top:48px;width:140px;height:140px;background:#58595b}
.copyright{top:2443px;height:50px;background:var(--blue-dark);color:#e6eef8;font-size:13px;text-align:center;line-height:50px}
</style>
</head>
<body>
<div class="page">

<header class="site-header">
  <div class="brand"><span class="brand-square"></span><span class="brand-name">Vormalux</span></div>
  <div class="top-contacts">
    <span><svg width="22" height="18" viewBox="0 0 22 18"><rect x="0" y="0" width="16" height="11" rx="2" fill="#ef0315"/><rect x="6" y="5" width="16" height="10" rx="2" fill="#fb3a37"/></svg>Talk/Chat Now</span>
    <span><svg width="16" height="16" viewBox="0 0 16 16"><path d="M3 1l3 3-2 2c1 2 3 4 5 5l2-2 3 3-2 3C7 15 1 9 1 3z" fill="#ef0315"/></svg>012.345.6789</span>
  </div>
  <nav class="main-nav"><span class="active">HOME</span><span>PRODUCT</span><span>COMPANY</span><span>NEWS</span><span>CONTACT US</span></nav>
</header>

<section class="hero" role="img" aria-label="Close-up photograph of a glowing green processor chip on a blue circuit board">
  <div class="hero-caption">High-Performance Interface Enables Early and Accurate Power<br>Profiling of Real-Time Applications</div>
</section>

<section class="welcome">
  <h2 class="section-title"><span class="title-square"></span>Welcome To Vormalux</h2>
  <div class="divider"></div>
  <p class="lead">Lorem ipsum dolor sit amet, consectetuer adipiscing elit, sed diam nonummy nibh euismod tincidunt ut laoreet dolore magna aliquam erat volutpat. Ut wisi enim ad minim veniam, quis nostrud exercitation ullamcorper suscipit lobortis nisl ut aliquip ex ea commodo consequat. Duis aute eummutation ullamcorper suscipit lobortis nisl ut aliquip ex ea commodo consequat. Duis autem vel eummu iriure dolor in hendrerit in vulputate velit esse molestie consequat facilisi. Duis aute eummutation ullamcorper suscipit lobortis nisl ut aliquip ex ea commodo consequat. Duis autem vel eummu iriure dolor in hendrerit in vulputate</p>
  <div class="btn">READ MORE</div>
</section>

<section class="about">
  <h2 class="section-title"><svg width="34" height="30" viewBox="0 0 34 30"><circle cx="12" cy="18" r="8" fill="none" stroke="#2454a0" stroke-width="5" stroke-dasharray="4 2.3"/><circle cx="25" cy="8" r="5" fill="none" stroke="#2454a0" stroke-width="4" stroke-dasharray="3 1.8"/></svg>About Our Product</h2>
  <div class="divider"></div>
  <p class="lead">Lorem ipsum dolor sit amet, consectetuer adipiscing elit, sed diam nonummy nibh euismod tincidunt ut laoreet dolore magna aliquam erat volutpat. Ut wisi enim ad minim veniam, quis nostrud exerci tation ullamcorper suscipit lobortis nisl ut aliquip ex ea commodo consequat.</p>
  <div class="steps">
    <div class="step" style="left:117px">
      <svg width="146" height="146" viewBox="0 0 146 146"><path d="M0 0H120A26 26 0 0 0 146 26V146H26A26 26 0 0 0 0 120Z" fill="#2454a0"/><g fill="none" stroke="#fff" stroke-width="5"><rect x="53" y="53" width="40" height="40"/><path d="M60 53V38M73 53V38M86 53V38M60 93V108M73 93V108M86 93V108M53 60H38M53 73H38M53 86H38M93 60H108M93 73H108M93 86H108"/></g></svg>
      <div class="step-label">Reducing Dynamic Voltage<br>Drop &amp; In-rush Current</div>
    </div>
    <svg class="step-arrow" style="left:428px" width="60" height="20" viewBox="0 0 60 20"><path d="M0 10H56M48 3L57 10L48 17" fill="none" stroke="#ccc" stroke-width="3"/></svg>
    <div class="step" style="left:502px">
      <svg width="146" height="146" viewBox="0 0 146 146"><path d="M26 0H146V120A26 26 0 0 0 120 146H0V26A26 26 0 0 0 26 0Z" fill="#2454a0"/><g fill="none" stroke="#fff" stroke-width="6"><path d="M73 40L106 73L73 106L40 73Z"/><path d="M60 70H80V90M70 56V64"/></g></svg>
      <div class="step-label">Grid Marshal<br>Advantages</div>
    </div>
    <svg class="step-arrow" style="left:772px" width="60" height="20" viewBox="0 0 60 20"><path d="M0 10H56M48 3L57 10L48 17" fill="none" stroke="#ccc" stroke-width="3"/></svg>
    <div class="step" style="left:846px">
      <svg width="146" height="146" viewBox="0 0 146 146"><path d="M0 0H120A26 26 0 0 0 146 26V146H26A26 26 0 0 0 0 120Z" fill="#2454a0"/><g fill="none" stroke="#fff" stroke-width="3"><circle cx="44" cy="78" r="6"/><path d="M50 78H90L104 52M70 78L84 96H108M90 78L100 104M78 46V78"/></g></svg>
      <div class="step-label">Grid Marshal<br>Product Details</div>
    </div>
  </div>
</section>

<section class="inquiry">
  <h2 class="section-title"><svg width="32" height="32" viewBox="0 0 32 32"><path d="M4 28L6 20L22 4L28 10L12 26Z" fill="#fff"/></svg>Quick Inquiry</h2>
  <div class="divider"></div>
  <div class="field" style="left:98px;top:147px;width:317px">NAME</div>
  <div class="field" style="left:440px;top:147px;width:318px">EMAIL</div>
  <div class="field" style="left:784px;top:147px;width:316px">PHONE</div>
  <div class="field" style="left:98px;top:198px;width:832px">MESSAGE</div>
  <div class="submit">SUBMIT</div>
</section>

<section class="news">
  <h2 class="section-title"><svg width="30" height="30" viewBox="0 0 30 30"><rect x="2" y="2" width="26" height="26" fill="none" stroke="#2454a0" stroke-width="3"/><rect x="7" y="7" width="7" height="7" fill="#2454a0"/><path d="M17 9H23M17 13H23M7 18H23M7 22H23" stroke="#2454a0" stroke-width="2"/></svg>Latest News</h2>
  <div class="divider"></div>
  <svg style="position:absolute;left:38px;top:175px" width="30" height="60" viewBox="0 0 30 60"><path d="M28 2L2 30L28 58" fill="none" stroke="#bbb" stroke-width="2"/></svg>
  <svg style="position:absolute;left:1132px;top:175px" width="30" height="60" viewBox="0 0 30 60"><path d="M2 2L28 30L2 58" fill="none" stroke="#bbb" stroke-width="2"/></svg>
  <div class="news-item" style="left:98px">
    <div class="news-photo" role="img" aria-label="Photo of a hand holding a processor chip" style="background:linear-gradient(135deg,#1e6fb0,#c98d6a 55%,#3a7e3f)"></div>
    <div class="news-body"><h3>Lorem ipsum dolor sit amet nonumy nibh</h3>
      <div class="news-date"><svg width="12" height="12" viewBox="0 0 12 12"><rect x="1" y="2" width="10" height="9" fill="none" stroke="#2454a0" stroke-width="1.5"/><path d="M1 5H11" stroke="#2454a0"/></svg>26 Nov, 2015</div>
      <p>Duis aute eummutation ullamcorper suscipit lobortismi nisl ut aliquip ex ea commodo consequat. Duis autem ok vel eummu iriure facilis.. <b>[+]</b></p></div>
  </div>
  <div class="news-item" style="left:630px">
    <div class="news-photo" role="img" aria-label="Photo of a cleanroom technician at work" style="background:linear-gradient(135deg,#c9d3de,#eef1f4 50%,#9fb0c2)"></div>
    <div class="news-body"><h3>Lorem ipsum dolor sit amet nonumy nibh</h3>
      <div class="news-date"><svg width="12" height="12" viewBox="0 0 12 12"><rect x="1" y="2" width="10" height="9" fill="none" stroke="#2454a0" stroke-width="1.5"/><path d="M1 5H11" stroke="#2454a0"/></svg>26 Nov, 2015</div>
      <p>Duis aute eummutation ullamcorper suscipit lobortismi nisl ut aliquip ex ea commodo consequat. Duis autem ok vel eummu iriure facilis.. <b>[+]</b></p></div>
  </div>
</section>
<div class="news-sep"></div>

<footer class="site-footer">
  <div class="footer-col" style="left:98px;width:136px">
    <h4>Quick Links</h4>
    <ul class="quick-links"><li>Home</li><li>Product</li><li>Company</li><li>News</li><li>Contact Us</li></ul>
  </div>
  <div class="footer-col" style="left:326px;width:242px">
    <h4>Newsletter Signup</h4>
    <p>Subscribe to our newsletter..</p>
    <div class="email-box">Email Address</div>
    <div class="gray-btn">READ MORE</div>
  </div>
  <div class="footer-col" style="left:662px;width:210px">
    <h4>Contact Details</h4>
    <div class="contact-row"><svg width="12" height="16" viewBox="0 0 12 16"><path d="M6 0A6 6 0 0 1 12 6C12 10 6 16 6 16S0 10 0 6A6 6 0 0 1 6 0Z" fill="#fff"/><circle cx="6" cy="6" r="2" fill="#333"/></svg><span>Sed diam nonummy euismod<br>tincidunt ut laor - 12345.</span></div>
    <div class="contact-row"><svg width="14" height="14" viewBox="0 0 16 16"><path d="M3 1l3 3-2 2c1 2 3 4 5 5l2-2 3 3-2 3C7 15 1 9 1 3z" fill="#fff"/></svg><span>123.456.7890</span></div>
    <div class="contact-row"><svg width="14" height="12" viewBox="0 0 14 12"><rect x="0" y="1" width="14" height="10" fill="#fff"/><path d="M0 1L7 7L14 1" fill="none" stroke="#333"/></svg><span>info@vormalux.com</span></div>
  </div>
  <div class="footer-mark"></div>
</footer>
<section class="copyright">Copyright© 2016 Vormalux | All Rights Reserved</section>

</div>
</body>
</html>
```